International Chino Pant Manufacturer

We need modern packaging design for men's chino. All kinds of packaging designs are welcome.

The pant is folded and packaged in a poly bag. We require a label design for the brand name Tarvo. The main label will be attached by a string on the belt loop. the size of that label will 15cm in length and 5cm wide. This is the first label the customer see's when he picks up the garment. Therefore, we require an eye catching design for that. If required it could have certain information about the chino pant on the main label such as Comfort fit, Wrinkle-resistant, machine washable, luxury fabric. But, if you feel that adding the above information spoils the design of the label then it is not a must to include the above information. On the back of the label we like to include the information that this pant was manufactured in an Ecora Summit certified green plant and hence the damage to the environment because of the plant is nill.

The second label label is attached on to the waist band and the purpose of that label is to include the size of the pant such 32x32. The size of that label is 8cm in length and 4cm in width. There is no design on the back on this label it has to be blank.

Manufacturer

```html
<!DOCTYPE html>
<html lang="en">
<head>
<meta charset="utf-8">
<title>Tarvo Chino Hang Tags</title>
<link rel="stylesheet" href="https://fonts.googleapis.com/css2?family=Alfa+Slab+One&family=Special+Elite&family=Open+Sans:wght@800&display=swap">
<style>
  :root {
    --backdrop-light: #f4f4f4;
    --backdrop-dark: #a9abae;
    --tan: #d3bc8a;
    --tan-deep: #c9a35e;
    --ink: #141210;
    --paper-white: #ffffff;
    --stitch: #e6d7aa;
    --badge-ring: #1d1a16;
  }
  * { margin: 0; padding: 0; box-sizing: border-box; }
  html, body { width: 1200px; height: 1000px; overflow: hidden; }
  body {
    position: relative;
    background: linear-gradient(180deg, var(--backdrop-light) 0%, #dcdddf 45%, var(--backdrop-dark) 100%);
  }
  .hang-tag {
    position: absolute;
    top: 42px;
    width: 305px;
    height: 916px;
    border-radius: 0 0 42px 42px;
    overflow: hidden;
  }
  .hang-tag--back { left: 243px; }
  .hang-tag--front { left: 652px; }

  .denim-texture {
    position: absolute; inset: 0;
  }
  .hang-tag--back .denim-texture {
    background:
      linear-gradient(200deg, transparent 0 30%, rgba(20,18,16,.55) 38%, transparent 48%),
      linear-gradient(160deg, transparent 0 60%, rgba(20,18,16,.6) 70%, transparent 82%),
      var(--tan);
  }
  .hang-tag--front .denim-texture {
    background:
      linear-gradient(195deg, rgba(20,18,16,.55) 0 8%, transparent 18% 40%, rgba(20,18,16,.5) 52%, transparent 62%),
      linear-gradient(150deg, transparent 0 55%, rgba(20,18,16,.7) 66%, transparent 76%),
      linear-gradient(90deg, var(--tan) 0 60%, rgba(20,18,16,.35) 85%, var(--tan) 100%),
      var(--tan);
  }

  .info-panel {
    position: absolute;
    left: 19px; top: 28px;
    width: 266px; height: 850px;
    background: var(--tan-deep);
    border-radius: 14px 14px 40px 40px;
    opacity: .95;
  }
  .stitch-line {
    position: absolute;
    border: 3px dashed var(--stitch);
    border-radius: 8px 8px 32px 32px;
  }
  .hang-tag--back .stitch-line { left: 9px; top: 18px; right: 9px; bottom: 12px; opacity: .7; }
  .hang-tag--front .stitch-line { left: 12px; top: 202px; right: 14px; bottom: 18px; border-color: #d6c48f; }

  .brand-name {
    position: absolute;
    writing-mode: vertical-rl;
    font-family: "Alfa Slab One", serif;
    text-transform: uppercase;
    letter-spacing: 8px;
    line-height: 1;
  }
  .hang-tag--back .brand-name {
    left: 155px; top: 95px;
    font-size: 118px;
    color: var(--ink);
  }
  .hang-tag--front .brand-name {
    left: 88px; top: 138px;
    font-size: 112px;
    color: var(--paper-white);
    letter-spacing: 6px;
  }

  .eco-statement {
    position: absolute;
    left: 27px; top: 98px;
    writing-mode: vertical-rl;
    font-family: "Special Elite", monospace;
    font-size: 21px;
    line-height: 30px;
    color: var(--ink);
    height: 620px;
  }
  .eco-statement .line-first { display: block; text-align-last: justify; }

  .certificate-seal {
    position: absolute;
    left: 69px; top: 688px;
    width: 132px; height: 132px;
  }

  .feature-list {
    position: absolute;
    left: 90px; top: 605px;
    writing-mode: vertical-rl;
    font-family: "Open Sans", sans-serif;
    font-weight: 800;
    font-size: 22px;
    line-height: 34px;
    color: var(--paper-white);
    list-style: none;
  }
</style>
</head>
<body>
  <section class="hang-tag hang-tag--back">
    <div class="denim-texture" role="img" aria-label="Distressed tan and black chino fabric texture"></div>
    <div class="info-panel"></div>
    <div class="stitch-line"></div>
    <h2 class="brand-name">Tarvo</h2>
    <p class="eco-statement">
      this pant was manufactured in an<br>
      Ecora Summit certified green plant<br>
      and hence the damage to the<br>
      environment because of the plant is nill.
    </p>
    <svg class="certificate-seal" viewBox="0 0 132 132" aria-hidden="true">
      <circle cx="66" cy="66" r="64" fill="var(--badge-ring)"/>
    </svg>
  </section>

  <section class="hang-tag hang-tag--front">
    <div class="denim-texture" role="img" aria-label="Close-up of folded tan chino fabric with pocket and button, distressed print"></div>
    <div class="stitch-line"></div>
    <h1 class="brand-name">Tarvo</h1>
    <ul class="feature-list">
      <li>Comfort fit</li>
      <li>Wrinkle-resistant</li>
      <li>machine washable</li>
      <li>luxury fabric</li>
    </ul>
  </section>
</body>
</html>
```